Letterhead for 3 attorney Workers' Comp law firm

We are a 3 attorney law office. We specialize in Workers' Compensation. Our office represents workers who are injured on the job, and the estates of workers who are killed one the job.
When we started our office, we created our own letterhead & have been using it for years. We've just recently hired the 3rd attorney, and were going to just add his name to the letterhead, but have decided we wanted to get a professionally designed letterhead and business cards at this point.
We want something that looks clean and professional. It must look good in black and white because we often make multiple copies of our documents. We're hoping for a design that resonates confidence, reliability and experience.
The design must include the firm name: Dorrance & Pike, PLLC. We would like the PLLC to be small compared to the Dorrance & Pike graphic. We also want to incorporate the attorney names: Ulric Dorrance, Janet Pike, and Lyle Hagberg. Our current letterhead has our contact info in the footer at the bottom of the page. We like that design, but are open to the idea of having it at the top. We'll leave that at the discretion of the designer. Our contact info is as follows: 472 S. Larchmont Avenue, Suite 315 Bellingham, WA 98117 Phone: 360-514-2967, Fax: 360-521-6079, and our website: www.dorrancepike-law.example
Target Market(s)
Clients, courts, other legal offices, doctors offices. These are the people who see our letterhead most frequently. It's not so much for marketing purposes, mainly so that we have a professional image when sending out documents.
Industry/Entity Type
Law Firm
Contact Information for Business Card
On the back of the business card: it can be designed, or be a template for filling in appointment reminder information (i.e. date, time, etc)
Colors
Designer to choose colors to be used in the design.
Requirements
Must have
- Must have our firm name at the top.
- Must include the attorney names.
- Must have all of our contact information (can be at top or bottom - whatever looks best with the design)
Nice to have
- A strong, confident design
Should not have
- We don't want the design to be playful, cartoony or busy.

```html
<!DOCTYPE html>
<html lang="en">
<head>
<meta charset="utf-8">
<title>Dorrance &amp; Pike, PLLC — Letterhead</title>
<link rel="stylesheet" href="https://fonts.googleapis.com/css2?family=Source+Sans+3:wght@400;600;700&display=swap">
<style>
  :root {
    --paper: #ffffff;
    --ink: #111111;
    --trim: #555555;
  }
  html, body {
    margin: 0;
    padding: 0;
    width: 874px;
    height: 1200px;
    overflow: hidden;
    background: var(--paper);
  }
  .sheet {
    position: relative;
    width: 874px;
    height: 1200px;
    background: var(--paper);
    color: var(--ink);
    font-family: "Source Sans 3", "Myriad Pro", Arial, sans-serif;
  }
  .crop-marks {
    position: absolute;
    inset: 0;
  }
  .masthead {
    position: absolute;
    left: 61px;
    top: 103px;
    height: 56px;
    display: flex;
    align-items: stretch;
  }
  .firm-mark {
    width: 268px;
    display: flex;
    flex-direction: column;
    justify-content: center;
  }
  .firm-name {
    margin: 0;
    font-size: 29px;
    font-weight: 600;
    line-height: 1;
    letter-spacing: 0.2px;
    white-space: nowrap;
  }
  .firm-suffix {
    font-size: 11px;
    font-weight: 600;
    letter-spacing: 1px;
    margin-left: 5px;
    vertical-align: 12px;
  }
  .attorneys {
    margin: 7px 0 0;
    font-size: 8px;
    font-weight: 600;
    line-height: 1.15;
  }
  .attorneys .role {
    display: block;
    padding-left: 70px;
  }
  .divider {
    width: 1.5px;
    background: var(--ink);
    margin-left: 22px;
    margin-right: 18px;
  }
  .contact {
    font-style: normal;
    font-size: 13.5px;
    font-weight: 600;
    line-height: 16.5px;
    padding-top: 0;
    letter-spacing: -0.1px;
  }
  .contact span { display: block; white-space: nowrap; }
</style>
</head>
<body>
  <div class="sheet">
    <svg class="crop-marks" width="874" height="1200" viewBox="0 0 874 1200" aria-hidden="true">
      <g stroke="var(--trim)" stroke-width="0.8" fill="none">
        <line x1="44" y1="0" x2="44" y2="42"/>
        <line x1="0" y1="42" x2="24" y2="42"/>
        <line x1="830" y1="0" x2="830" y2="42"/>
        <line x1="850" y1="42" x2="874" y2="42"/>
        <line x1="44" y1="1159" x2="44" y2="1200"/>
        <line x1="0" y1="1159" x2="24" y2="1159"/>
        <line x1="830" y1="1159" x2="830" y2="1200"/>
        <line x1="850" y1="1159" x2="874" y2="1159"/>
      </g>
    </svg>

    <header class="masthead">
      <div class="firm-mark">
        <h1 class="firm-name">Dorrance &amp; Pike<span class="firm-suffix">PLLC</span></h1>
        <p class="attorneys">Ulric Dorrance, Janet Pike &amp; Lyle Hagberg<span class="role">Attorneys</span></p>
      </div>
      <div class="divider" aria-hidden="true"></div>
      <address class="contact">
        <span>472 S. Larchmont Avenue,</span>
        <span>Suite 315 Bellingham, WA 98117</span>
        <span>Phone: 360-514-2967, Fax: 360-521-6079,</span>
        <span>website: www.dorrancepike-law.example</span>
      </address>
    </header>
  </div>
</body>
</html>
```